KTR Business Cards

We require business cards for our business. We would like a matte black back to the card, with our logo centred in the middle. The front side of the card is open to design.

Target Market(s)

Clients looking for legal services (professional)

Industry/Entity Type

Legal

Contact Information for Business Card

Dario Velkenor
Partner
Mobile: 0471 386 524
Email: dario@ktrlaw.co
Website: www.ktrlaw.co
Level 3, 118 Pembury Street
Sydney NSW 2000

Font styles to use
Other font styles liked:
• Avenir

Colors
f04a50
ffffff
1b1b1b

Requirements
Must have
• Black back with logo included in the centre of the card.
• Our font is Avenir.

```html
<!DOCTYPE html>
<html lang="en">
<head>
<meta charset="utf-8">
<title>KTR Legal — Business Cards</title>
<link rel="stylesheet" href="https://fonts.googleapis.com/css2?family=Nunito+Sans:wght@400;600;700;800&display=swap">
<style>
  :root {
    --brand-red: #c8163f;
    --accent-red: #f04a50;
    --ink: #1b1b1b;
    --paper: #ffffff;
    --muted: #4a4a4a;
    --rule: #2a2a2a;
    --stage: #2b2b2b;
  }
  * { box-sizing: border-box; margin: 0; padding: 0; }
  html, body {
    width: 1200px; height: 960px; overflow: hidden;
    background: var(--stage);
    font-family: "Nunito Sans", "Avenir", Arial, sans-serif;
  }
  .sheet {
    width: 1200px; height: 960px;
    display: flex; flex-direction: column; align-items: center; justify-content: center;
    gap: 40px;
  }
  .card {
    position: relative;
    width: 700px; height: 428px;
    border-radius: 4px;
    overflow: hidden;
    box-shadow: 0 10px 30px rgba(0,0,0,0.35);
  }

  /* Back */
  .card--back { background: var(--ink); }
  .card--back .wordmark {
    position: absolute; left: 50%; top: 170px; transform: translateX(-50%);
  }
  .card--back .wordmark__name { color: var(--paper); }
  .card--back .site {
    position: absolute; left: 0; right: 0; top: 300px;
    text-align: center; color: var(--paper);
    font-size: 15px; letter-spacing: 5px; font-weight: 600;
  }
  .site__domain { color: var(--brand-red); }

  /* Wordmark */
  .wordmark { display: flex; align-items: center; gap: 16px; }
  .wordmark__square { width: 34px; height: 34px; background: var(--brand-red); }
  .wordmark__name {
    font-size: 40px; font-weight: 800; letter-spacing: 1px; line-height: 1;
    text-transform: uppercase;
  }

  /* Front */
  .card--front { background: var(--paper); }
  .card--front .wordmark { position: absolute; left: 430px; top: 118px; }
  .card--front .wordmark__name { color: var(--ink); font-size: 34px; }
  .holder { position: absolute; left: 52px; top: 126px; }
  .holder__name {
    color: var(--brand-red); font-size: 25px; font-weight: 800;
    text-transform: uppercase; letter-spacing: 0.5px; line-height: 1.1;
  }
  .holder__role {
    color: var(--muted); font-size: 15px; text-transform: uppercase; margin-top: 2px;
  }
  .divider-rule {
    position: absolute; left: 52px; right: 0; top: 196px; height: 1px; background: var(--rule);
  }
  .divider-rule__accent {
    position: absolute; left: 0; top: -2px; width: 92px; height: 5px; background: var(--brand-red);
  }
  .contacts {
    position: absolute; left: 52px; top: 222px; list-style: none;
  }
  .contacts li {
    display: flex; align-items: center; gap: 10px;
    font-size: 15px; color: var(--ink); height: 28px;
  }
  .contacts svg { width: 16px; height: 16px; flex: none; }
  .column-rule {
    position: absolute; left: 238px; top: 262px; width: 1px; height: 70px; background: #bdbdbd;
  }
  .address {
    position: absolute; left: 262px; top: 278px;
    font-style: normal; font-size: 16px; line-height: 1.45; color: var(--ink);
  }
</style>
</head>
<body>
<main class="sheet">

  <section class="card card--back" aria-label="Card back">
    <div class="wordmark">
      <span class="wordmark__square"></span>
      <span class="wordmark__name">KTR Legal</span>
    </div>
    <p class="site">www.<span class="site__domain">ktrlaw</span>.co</p>
  </section>

  <section class="card card--front" aria-label="Card front">
    <div class="holder">
      <h1 class="holder__name">Dario Velkenor</h1>
      <p class="holder__role">Partner</p>
    </div>
    <div class="divider-rule"><span class="divider-rule__accent"></span></div>

    <ul class="contacts">
      <li>
        <svg viewBox="0 0 16 16" aria-hidden="true"><circle cx="8" cy="8" r="8" fill="var(--brand-red)"/><rect x="5.5" y="3.5" width="5" height="9" rx="1" fill="none" stroke="#fff" stroke-width="1.2"/><circle cx="8" cy="11" r="0.7" fill="#fff"/></svg>
        0471 386 524
      </li>
      <li>
        <svg viewBox="0 0 16 16" aria-hidden="true"><circle cx="8" cy="8" r="8" fill="var(--brand-red)"/><rect x="4" y="5" width="8" height="6" fill="none" stroke="#fff" stroke-width="1.2"/><path d="M4 5l4 3.5L12 5" fill="none" stroke="#fff" stroke-width="1.2"/></svg>
        dario@ktrlaw.co
      </li>
      <li>
        <svg viewBox="0 0 16 16" aria-hidden="true"><circle cx="8" cy="8" r="8" fill="var(--brand-red)"/><circle cx="8" cy="8" r="4.5" fill="none" stroke="#fff" stroke-width="1"/><ellipse cx="8" cy="8" rx="2" ry="4.5" fill="none" stroke="#fff" stroke-width="1"/><path d="M3.5 8h9" stroke="#fff" stroke-width="1"/></svg>
        www.ktrlaw.co
      </li>
    </ul>

    <span class="column-rule"></span>
    <address class="address">
      Level 3, 118 Pembury Street<br>
      Sydney NSW 2000
    </address>

    <div class="wordmark">
      <span class="wordmark__square"></span>
      <span class="wordmark__name">KTR Legal</span>
    </div>
  </section>

</main>
</body>
</html>
```